Northbound's green Wagon Van Decal

Good day,
I am looking for a decal or wrap for my work van. The name of the Business is Northbound’s Green Wagon, and we are a van rental company with a provided driver. We offer transport, delivery and expediting services to our customers.
The Van is a 2024 Vexa Cargoline 3400 159in wb ext. and its red.
I do not want a fully 360 top to bottom van decal just the region in green on both side of the van and in the back for the decal. See attached.
The following is text information that needs to be added on the decal.
- Name of the Business is Northbound’s Green Wagon
- Company motto: Your buddy behind the wheel
- Van Rental with driver
- Evenings and weekends.
The costumer can contact us by:
Email: Rosedale@northboundsgreenwagon.com
Phone or Text at: 555-274-9061
Keep in mind that the van is RED. If I cannot Invision what your wrap will look like on the Van there’s a high chance it won’t be chosen.
Thank you for your time.
Updates
Low design quality
Good day,
I have change the requirement of the project. it should be a lot more manageable and foster more creativity from designer.
Please have a look at the revise brief if you're interested.
Industry/Entity Type
Moving business
Look and feel
Each slider illustrates characteristics of the customer's brand and the style your logo design should communicate.

```html
<!DOCTYPE html>
<html lang="en">
<head>
<meta charset="UTF-8">
<title>Northbound's Green Wagon – Van Side Decal</title>
<link href="https://fonts.googleapis.com/css2?family=Roboto+Condensed:wght@500;700&family=Roboto:wght@400;500;700;900&display=swap" rel="stylesheet">
<style>
  :root {
    --canvas-bg: #ececec;
    --brand-red: #d8141a;
    --deep-red: #9e0d12;
    --ink: #111111;
    --paper: #ffffff;
  }
  html, body {
    margin: 0;
    padding: 0;
    width: 1200px;
    height: 668px;
    overflow: hidden;
    background: var(--canvas-bg);
  }
  .decal {
    position: absolute;
    left: 50px;
    top: 229px;
    width: 1100px;
    height: 210px;
    font-family: "Roboto", sans-serif;
  }
  .decal-shapes {
    position: absolute;
    inset: 0;
  }
  .brand-mark {
    position: absolute;
    left: 22px;
    top: 36px;
    width: 196px;
    display: flex;
    flex-direction: column;
    align-items: center;
    gap: 10px;
  }
  .brand-mark-dot {
    width: 70px;
    height: 70px;
    border-radius: 50%;
    background: var(--brand-red);
  }
  .brand-mark-name {
    font-family: "Roboto", sans-serif;
    font-weight: 500;
    font-size: 14px;
    color: var(--ink);
    text-align: center;
    line-height: 1.2;
  }
  .business-name {
    position: absolute;
    left: 236px;
    top: 18px;
    width: 500px;
    margin: 0;
    text-align: center;
    font-family: "Roboto", sans-serif;
    font-weight: 900;
    font-size: 50px;
    line-height: 1.12;
    color: var(--ink);
    letter-spacing: -0.5px;
  }
  .motto {
    position: absolute;
    left: 808px;
    top: 6px;
    width: 290px;
    margin: 0;
    text-align: center;
    color: var(--paper);
    font-size: 27px;
    line-height: 1.12;
    font-weight: 400;
  }
  .motto strong { font-weight: 700; }
  .services {
    position: absolute;
    left: 790px;
    top: 90px;
    margin: 0;
    padding: 0;
    list-style: none;
    font-family: "Roboto Condensed", sans-serif;
    font-weight: 700;
    font-size: 19px;
    line-height: 1.42;
    color: var(--paper);
  }
  .services li::before {
    content: "";
    display: inline-block;
    width: 7px;
    height: 7px;
    border-radius: 50%;
    background: var(--ink);
    margin-right: 9px;
    vertical-align: middle;
  }
  .contact-bar {
    position: absolute;
    left: 250px;
    top: 150px;
    width: 840px;
    height: 56px;
    display: flex;
    align-items: center;
    gap: 22px;
    color: var(--paper);
    font-weight: 500;
  }
  .contact-item {
    display: flex;
    align-items: center;
    gap: 9px;
  }
  .contact-phone { font-size: 31px; }
  .contact-email { font-size: 27px; }
  .contact-icon { flex: none; }
</style>
</head>
<body>
  <div class="decal">
    <svg class="decal-shapes" width="1100" height="210" viewBox="0 0 1100 210" aria-hidden="true">
      <polygon class="panel-white" points="0,0 802,0 760,150 0,150 0,210 228,210 228,150" fill="#ffffff"/>
      <rect x="0" y="0" width="230" height="210" fill="#ffffff"/>
      <polygon class="panel-red" points="806,0 1100,0 1100,150 764,150" fill="#d8141a"/>
      <polygon class="panel-deep-red" points="785,84 1100,84 1100,150 767,150" fill="#9e0d12"/>
      <line x1="804" y1="0" x2="762" y2="150" stroke="#111111" stroke-width="4"/>
      <polygon class="contact-band" points="240,150 1100,150 1100,208 228,208" fill="#111111"/>
    </svg>

    <div class="brand-mark">
      <div class="brand-mark-dot"></div>
      <div class="brand-mark-name">Northbound’s Green Wagon</div>
    </div>

    <h1 class="business-name">Northbound’s<br>Green Wagon</h1>

    <p class="motto">Your <strong>BUDDY</strong><br>behind the <strong>WHEEL</strong></p>

    <ul class="services">
      <li>VAN RENTAL WITH DRIVER</li>
      <li>EVENINGS AND WEEKENDS</li>
    </ul>

    <div class="contact-bar">
      <div class="contact-item contact-phone">
        <svg class="contact-icon" width="26" height="26" viewBox="0 0 24 24" aria-hidden="true">
          <path d="M6.6 10.8c1.4 2.8 3.8 5.1 6.6 6.6l2.2-2.2c.3-.3.7-.4 1-.2 1.1.4 2.3.6 3.6.6.6 0 1 .4 1 1V20c0 .6-.4 1-1 1C10.6 21 3 13.4 3 4c0-.6.4-1 1-1h3.5c.6 0 1 .4 1 1 0 1.3.2 2.5.6 3.6.1.3 0 .7-.2 1z" fill="#d8141a"/>
        </svg>
        <span>555-274-9061</span>
      </div>
      <div class="contact-item contact-email">
        <svg class="contact-icon" width="30" height="22" viewBox="0 0 30 22" aria-hidden="true">
          <rect x="1.5" y="1.5" width="27" height="19" fill="none" stroke="#d8141a" stroke-width="3"/>
          <polyline points="2,2 15,12 28,2" fill="none" stroke="#d8141a" stroke-width="3"/>
        </svg>
        <span>Rosedale@northboundsgreenwagon.com</span>
      </div>
    </div>
  </div>
</body>
</html>
```